Website Design for a "Talent Recruitment Agency"

We are looking for a website design for the website of our "Talent Recruitment Agency"; which is called "Crestway Hub".
Our recruitment website "Crestway Hub" will be focusing on: "Crestway Hub: Linking People & Firms in Switzerland"; which means our target audience is two-folded:
(i) TALENT - that is currently residing in- or outside of Switzerland, and is open for and interested in the "Swiss Job Market".
(ii) COMPANIES - that are looking for talent for specific job vacancies in Switzerland.
With our "Crestway Hub" approach we inted to focus on Membership & Partnership:
(a)"Membership"(TALENT)
and
(b)"Partnership"(COMPANIES)
Some of the competitor sites we like are:
• www.plimora42.dk
• www.qelvo.ch
• www.brandolix.ch/en
A sitemap example of our website is attached.
Also attached is a "Crestway Hub" logo in .eps format and one in .jpeg format.
We very much look forward to receive your creative ideas.
Best regards,
Crestway Hub
Crestway Hub: Linking People & Firms in Switzerland.
Website: crestwayhub.ch - Twitter: CrestwayHubCH
Target Market(s)
(i) TALENT (with around 0-10 years of working experience), currently residing in- or outside of Switzerland, but eligible to work in Switzerland.
(ii) COMPANIES (national or international) that are based in Switzerland.
Industry/Entity Type
Recruitment

```html
<!DOCTYPE html>
<html lang="en">
<head>
<meta charset="utf-8">
<title>Crestway Hub</title>
<link href="https://fonts.googleapis.com/css2?family=Lato:wght@400;700&family=Bitter:wght@700&display=swap" rel="stylesheet">
<style>
:root{
  --blue:#0a93cf;
  --blue-dark:#0779ad;
  --orange:#ff6a2b;
  --orange-soft:rgba(240,110,40,.88);
  --text:#3a3a3a;
  --muted:#666;
  --line:#cfcfcf;
  --white:#fff;
}
*{box-sizing:border-box;margin:0;padding:0}
html,body{width:1200px;height:1108px;overflow:hidden;background:var(--white);font-family:"Lato",sans-serif;color:var(--text)}
.stage{position:absolute;left:9px;top:0;width:1280px;height:1200px;transform:scale(.9233);transform-origin:0 0}
.abs{position:absolute}
.brand{left:140px;top:28px;display:flex;align-items:center;gap:12px}
.brand-dot{width:58px;height:58px;border-radius:50%;background:var(--blue)}
.brand-name{font-size:32px;font-weight:700;color:var(--blue)}
.lang{right:140px;top:20px;display:flex;align-items:center;gap:6px;font-size:14px;color:var(--muted)}
.flag{width:30px;height:22px;border:1px solid #999}
.flag.en{background:#2c3f8f}
.flag.de{background:linear-gradient(#111 33%,#d00 33% 66%,#fc0 66%)}
.contact-top{right:140px;top:58px;display:flex;align-items:center;gap:8px;color:var(--muted)}
.contact-top .phone{font-size:17px;margin-right:16px}
.contact-top .mail{font-size:15px}
.nav{left:140px;top:108px;width:1000px;height:45px;background:var(--blue);display:flex}
.nav a{color:var(--white);text-decoration:none;font-weight:700;font-size:15px;display:flex;align-items:center;justify-content:center;border-right:1px solid var(--blue-dark)}
.nav a.active{background:var(--orange)}
.nav a:last-child{border:none}
.hero{left:140px;top:153px;width:1000px;height:400px;background:linear-gradient(180deg,#e9e7e3 0%,#b9b1a8 45%,#4a4440 100%)}
.arrow{width:26px;height:26px;border-radius:50%;background:rgba(200,200,200,.8);display:flex;align-items:center;justify-content:center}
.caption{left:703px;top:362px;width:437px;height:85px;background:var(--orange-soft);padding:8px 15px;font-family:"Bitter",serif;font-weight:700;font-size:25px;line-height:35px;color:var(--white);text-shadow:1px 1px 2px rgba(0,0,0,.35)}
.card{top:525px;width:292px;height:151px;background:var(--white);border:1px solid var(--line);border-radius:6px;text-align:center;box-shadow:0 8px 8px -6px rgba(0,0,0,.18)}
.card-badge{position:absolute;left:94px;top:-44px;width:104px;height:104px;border-radius:50%;background:var(--white);border:1px solid var(--line);clip-path:inset(0 0 58% 0)}
.card-icon{position:absolute;left:120px;top:-30px}
.card h2{margin-top:30px;font-size:26px;font-weight:400;color:var(--blue)}
.card p{margin:6px 8px 0;font-size:14px;line-height:19.5px;color:#444}
.btn{display:inline-block;background:var(--blue);color:var(--white);font-size:14px;padding:4px 11px;border-radius:2px;text-decoration:none}
.card .btn{position:absolute;left:50%;transform:translateX(-50%);bottom:-13px}
.welcome{left:140px;top:725px;width:1000px}
.welcome h1{font-size:26px;font-weight:400;color:var(--blue);padding:0 2px 4px;border-bottom:1px solid var(--line)}
.welcome .lead{color:var(--orange);font-size:14px;margin:10px 0 10px}
.photo{float:left;width:185px;height:121px;margin:0 13px 4px 0;border:4px solid #ccc;background:linear-gradient(135deg,#cfd6dc,#f0ebe6 55%,#a9b4bc)}
.welcome p.body{font-size:14px;line-height:21px;color:var(--text)}
.welcome .btn{margin-top:8px}
.footer{left:140px;top:1030px;width:1000px;height:152px;background:var(--blue);border-top:3px solid var(--orange);color:var(--white);font-weight:700;font-size:14px;text-align:center}
.foot-nav{margin-top:10px;word-spacing:2px}
.foot-nav span{margin:0 10px;font-weight:400}
.foot-info{display:flex;justify-content:center;gap:30px;margin-top:12px;font-size:13px;line-height:17px;text-align:left}
.foot-info div{display:flex;gap:8px;align-items:flex-start}
.social{display:flex;justify-content:center;gap:10px;margin-top:6px}
.social i{width:30px;height:30px;border-radius:50%;background:var(--white)}
.copy{position:absolute;left:0;bottom:0;width:100%;height:37px;border-top:1px solid #2aa6dc;line-height:36px}
</style>
</head>
<body>
<div class="stage">
  <div class="abs brand"><span class="brand-dot"></span><span class="brand-name">Crestway Hub</span></div>
  <div class="abs lang">Multi-language Support: <span class="flag en"></span><span class="flag de"></span></div>
  <div class="abs contact-top">
    <svg width="18" height="18" viewBox="0 0 24 24"><path fill="#ff6a2b" d="M6.6 10.8a15 15 0 0 0 6.6 6.6l2.2-2.2c.3-.3.7-.4 1-.2 1.1.4 2.3.6 3.6.6.6 0 1 .4 1 1V20c0 .6-.4 1-1 1A17 17 0 0 1 3 4c0-.6.4-1 1-1h3.5c.6 0 1 .4 1 1 0 1.3.2 2.5.6 3.6.1.3 0 .7-.2 1z"/></svg>
    <span class="phone">(012) 345 6789</span>
    <svg width="16" height="12" viewBox="0 0 16 12"><rect width="16" height="12" fill="#ff6a2b"/><path d="M0 0l8 6 8-6" stroke="#fff" fill="none" stroke-width="1.5"/></svg>
    <span class="mail">info@crestwayhub.ch</span>
  </div>
  <nav class="abs nav">
    <a class="active" style="width:140px">HOME</a>
    <a style="width:169px">ABOUT</a>
    <a style="width:172px">TALENT</a>
    <a style="width:203px">COMPANIES</a>
    <a style="width:152px">JOBS</a>
    <a style="width:164px">CONTACT</a>
  </nav>
  <div class="abs hero" role="img" aria-label="Photo of a smiling group of business professionals"></div>
  <div class="abs arrow" style="left:154px;top:322px"><svg width="10" height="12"><path d="M8 1L2 6l6 5" stroke="#fff" stroke-width="2" fill="none"/></svg></div>
  <div class="abs arrow" style="left:1100px;top:322px"><svg width="10" height="12"><path d="M2 1l6 5-6 5" stroke="#fff" stroke-width="2" fill="none"/></svg></div>
  <div class="abs caption">Crestway Hub: Linking People<br>&amp; Firms in Switzerland</div>

  <div class="abs card" style="left:171px">
    <span class="card-badge"></span>
    <svg class="card-icon" width="52" height="46" viewBox="0 0 52 46"><g fill="#ff6a2b"><circle cx="10" cy="12" r="5"/><circle cx="26" cy="7" r="6"/><circle cx="42" cy="12" r="5"/><rect x="3" y="19" width="14" height="27" rx="4"/><rect x="18" y="15" width="16" height="31" rx="4"/><rect x="35" y="19" width="14" height="27" rx="4"/></g></svg>
    <h2>Talent</h2>
    <p>Lorem ipsum dolor sit amet, consectetur adi pis icing elit, sed do eiusmod temporsum dolor sit ameto eiusmo...</p>
    <a class="btn">Read More</a>
  </div>
  <div class="abs card" style="left:494px">
    <span class="card-badge"></span>
    <svg class="card-icon" width="56" height="46" viewBox="0 0 56 46"><rect x="14" y="0" width="28" height="46" fill="#ff6a2b"/><rect x="0" y="16" width="56" height="30" fill="#ff6a2b"/><g fill="#fff"><rect x="19" y="5" width="5" height="4"/><rect x="32" y="5" width="5" height="4"/><rect x="5" y="21" width="5" height="4"/><rect x="19" y="21" width="5" height="4"/><rect x="32" y="21" width="5" height="4"/><rect x="46" y="21" width="5" height="4"/><rect x="5" y="31" width="5" height="4"/><rect x="19" y="31" width="5" height="4"/><rect x="32" y="31" width="5" height="4"/><rect x="46" y="31" width="5" height="4"/></g></svg>
    <h2>Companies</h2>
    <p>Lorem ipsum dolor sit amet, consectetur adi pis icing elit, sed do eiusmod temporsum dolor sit ameto eiusmo...</p>
    <a class="btn">Read More</a>
  </div>
  <div class="abs card" style="left:818px">
    <span class="card-badge"></span>
    <svg class="card-icon" width="52" height="46" viewBox="0 0 52 46"><path d="M18 8V3h16v5" stroke="#ff6a2b" stroke-width="4" fill="none"/><rect x="2" y="9" width="48" height="36" fill="#ff6a2b"/><rect x="2" y="24" width="48" height="2" fill="#fff"/><rect x="22" y="21" width="8" height="8" fill="#fff"/></svg>
    <h2>Jobs</h2>
    <p>Lorem ipsum dolor sit amet, consectetur adi pis icing elit, sed do eiusmod temporsum dolor sit ameto eiusmo...</p>
    <a class="btn">Read More</a>
  </div>

  <section class="abs welcome">
    <h1>Welcome</h1>
    <p class="lead">Duis autem vel eum iriure dolor in hendrerit in vulputate velit vel illum dolore eu feugiat nulla</p>
    <div class="photo" role="img" aria-label="Photo of a smiling young woman giving a thumbs up in an office"></div>
    <p class="body">Lorem ipsum dolor sit amet, consectetuer adipiscing elit, sed diam nonummy n euismod tincidunt ut laoreet dolore magn aliquam erat volutpat. Ut wisi enim ad minim veniam, quis nostrud exerci tation ullamcorper suscipit lobortis nisl ut aliquip ex commodo consequat. Duis autem vel eum iriure d hendrerit in vulputate velit esse mol consequat, vel illum dolore eu feugiat nulla facilisis at vero eros et accumsan et iusto odi dignissim qui blandit praesent luptatum zzril delenit augue duis dolore te feugait nulla facilisi. quis nostrud exerci tation ullamcorper suscipit lobortis nisl ut aliquip ex commodo consequat. Duis autem vel eum iriu hendrerit in vulputate velit esse mol consequat.</p>
    <p class="body" style="clear:both;margin-top:5px">Lorem ipsum dolor sit amet, consectetuer adipiscing elit, sed diam nonummy n euismod tincidunt ut laoreet dol magna aliquam erat volutpat. Ut wisi enim ad minim veniam, quis nostrud exerci tation ullamcorper suscipit lobortis ni aliquip ex ea commodo consequat.</p>
    <a class="btn">Read More</a>
  </section>

  <footer class="abs footer">
    <div class="foot-nav">HOME<span>|</span>ABOUT<span>|</span>TALENT<span>|</span>COMPANIES<span>|</span>JOBS<span>|</span>EVENTS<span>|</span>CONTACT</div>
    <div class="foot-info">
      <div><svg width="20" height="18" viewBox="0 0 20 18"><path d="M10 0L0 9h3v9h5v-6h4v6h5V9h3z" fill="#ff6a2b"/></svg><span>Lorem ipsum dolor sit amet, adipiscing<br>elit,</span></div>
      <div><svg width="20" height="20" viewBox="0 0 20 20"><circle cx="10" cy="10" r="9" stroke="#ff6a2b" stroke-width="2" fill="none"/><path d="M7 5l2 3-1 1a7 7 0 0 0 3 3l1-1 3 2-1 2c-4 0-8-4-8-8z" fill="#ff6a2b"/></svg><span>012.345.6789</span></div>
      <div><svg width="20" height="20" viewBox="0 0 20 20"><circle cx="10" cy="10" r="8.5" stroke="#ff6a2b" stroke-width="2" fill="none"/><circle cx="10" cy="10" r="3.5" stroke="#ff6a2b" stroke-width="2" fill="none"/></svg><span>info@crestwayhub.ch</span></div>
    </div>
    <div class="social"><i></i><i></i><i></i><i></i></div>
    <div class="copy">© 2014 Crestway Hub. All Right Reserved.&nbsp; T&amp;Cs &nbsp;&nbsp;| Disclaimer</div>
  </footer>
</div>
</body>
</html>
```